We Need a Letterhead + Fax Cover Sheet for Kestrel Works

LETTERHEAD:
- Simple letterhead. Please provide an editable .doc file apart from usual Source Files. Logo Files attached for your use.
- Please place our logo on the upper right corner of the page. You may add some sort of graphic, or light colored background (depends on what looks good).
- Footer should include:
Kestrel Works, LLC
418 Wrenfield Ave. Suite 172
Mobile, AL 36619

FAX COVER SHEET:
- Have the logo placed here, should be large, maybe an eight of the page.
- Put:
From:
To:
Phone Number:
Fax Number:

*Still needs some details, will update you because working on the website, etc.

Kestrel Harbor Staffing Services

```html
<!DOCTYPE html>
<html lang="en">
<head>
<meta charset="utf-8">
<title>Kestrel Works – Letterhead and Fax Cover Sheet</title>
<link rel="stylesheet" href="https://fonts.googleapis.com/css2?family=Lato:wght@400;700&family=Roboto:wght@300;400&display=swap">
<style>
  :root {
    --backdrop: #d3d3d3;
    --paper: #ffffff;
    --ink: #1e1e1e;
    --label: #444444;
    --fax-grey: #8c8c8c;
    --brand-green: #8aa83a;
    --brand-blue: #0c71b3;
    --rule: #555555;
  }
  * { margin: 0; padding: 0; box-sizing: border-box; }
  html, body { width: 1200px; height: 1200px; overflow: hidden; }
  body { background: var(--backdrop); position: relative; font-family: "Roboto", Arial, sans-serif; color: var(--ink); }

  .sheet { position: absolute; top: 230px; width: 465px; height: 656px; background: var(--paper); }
  .sheet--letterhead { left: 113px; }
  .sheet--fax { left: 646px; }

  .brand-mark { position: absolute; text-align: center; color: var(--brand-blue); font-family: "Lato", Arial, sans-serif; font-weight: 700; line-height: 1.05; text-transform: uppercase; }
  .sheet--letterhead .brand-mark { left: 330px; top: 28px; width: 100px; font-size: 12px; }
  .sheet--fax .brand-mark { left: 282px; top: 42px; width: 150px; font-size: 18px; }
  .brand-mark .brand-sub { display: block; margin-top: 4px; font-size: 0.55em; letter-spacing: 0.04em; }

  .footer-address { position: absolute; left: 40px; top: 619px; font-family: "Lato", Arial, sans-serif; font-size: 6.6px; line-height: 1.3; color: var(--ink); }
  .footer-band { position: absolute; left: 0; bottom: 0; width: 100%; height: 11px; background: var(--brand-green); }
  .footer-band::after { content: ""; position: absolute; top: 0; right: 0; width: 88px; height: 11px; background: var(--brand-blue); border-left: 3px solid var(--paper); transform-origin: bottom left; clip-path: polygon(8px 0, 100% 0, 100% 100%, 0 100%); }

  .fax-title { position: absolute; left: 44px; top: 26px; font-family: "Roboto", Arial, sans-serif; font-weight: 300; font-size: 58px; color: var(--fax-grey); letter-spacing: -1px; }

  .fax-fields { position: absolute; left: 48px; top: 213px; width: 370px; }
  .field-label { position: absolute; font-size: 7px; color: var(--label); text-transform: uppercase; }
  .field-label--main { font-size: 9px; text-transform: none; }
  .field-rule { position: absolute; left: 0; width: 370px; border-top: 1px dotted var(--rule); }

  .comments-label { position: absolute; left: 48px; top: 346px; font-size: 9px; color: var(--label); }
  .comments-rule { position: absolute; left: 48px; top: 473px; width: 370px; border-top: 1px solid var(--rule); }

  .status-list { position: absolute; left: 48px; top: 491px; list-style: none; }
  .status-item { display: flex; align-items: center; height: 23.5px; font-size: 8px; color: var(--ink); }
  .status-box { width: 13px; height: 13px; border: 1px solid var(--ink); margin-right: 7px; }
</style>
</head>
<body>

<section class="sheet sheet--letterhead" aria-label="Letterhead">
  <div class="brand-mark">Kestrel Harbor<span class="brand-sub">Staffing Services</span></div>
  <p class="footer-address">Kestrel Works, LLC &nbsp;|&nbsp; 418 Wrenfield Ave. Suite 172 &nbsp; Mobile, AL 36619<br>www.kestrelworks.com</p>
  <div class="footer-band"></div>
</section>

<section class="sheet sheet--fax" aria-label="Fax cover sheet">
  <h1 class="fax-title">FAX</h1>
  <div class="brand-mark">Kestrel Harbor<span class="brand-sub">Staffing Services</span></div>

  <div class="fax-fields">
    <span class="field-label field-label--main" style="left:0;top:0">TO:</span>
    <span class="field-label field-label--main" style="left:172px;top:0">FROM:</span>
    <span class="field-label" style="left:172px;top:23px">Pages</span>
    <div class="field-rule" style="top:34px"></div>
    <span class="field-label" style="left:0;top:43px">Fax</span>
    <span class="field-label" style="left:172px;top:43px">Fax</span>
    <div class="field-rule" style="top:55px"></div>
    <span class="field-label" style="left:0;top:61px">Phone</span>
    <span class="field-label" style="left:172px;top:61px">Phone</span>
    <div class="field-rule" style="top:76px"></div>
    <span class="field-label" style="left:0;top:82px">CC</span>
    <div class="field-rule" style="top:97px"></div>
    <span class="field-label" style="left:0;top:102px">RE</span>
    <div class="field-rule" style="top:117px"></div>
  </div>

  <p class="comments-label">Comments:</p>
  <div class="comments-rule"></div>

  <ul class="status-list">
    <li class="status-item"><span class="status-box"></span>Urgent</li>
    <li class="status-item"><span class="status-box"></span>Please Preview</li>
    <li class="status-item"><span class="status-box"></span>Please Comment</li>
    <li class="status-item"><span class="status-box"></span>For your records</li>
  </ul>

  <p class="footer-address">Kestrel Works, LLC &nbsp;|&nbsp; 418 Wrenfield Ave. Suite 172 &nbsp; Mobile, AL 36619<br>www.kestrelworks.com</p>
  <div class="footer-band"></div>
</section>

</body>
</html>
```